Flyer for Addiction program

Hi There,There are two parts to this project.1. A double-sided flyer for my next 5-day treatment program for addictions and family trauma.2. A one-page cover for the front of the course folders to match the above flyer?I have put together an information folder. Here is the filecrate link;https://www.filecrate.com/sh/jn7lkly6wcqphpt/AACmad0pag08NeuT2pM27USPa?dl=0Included in the information folder is;1. Copy2. Selection of images3. Logos and Brand identity kit4. Examples of past flyers and folder coverPlease don't hesitate to contact me if you have any questions.RegardsRebecca

Colors

Designer to choose colors to be used in the design.

Requirements
Must have
• 2 pages flyer please.
• Contemporary / fresh design

```html
<!DOCTYPE html>
<html lang="en">
<head>
<meta charset="utf-8">
<title>Untangling the Family Pattern – Flyer</title>
<link href="https://fonts.googleapis.com/css2?family=Lato:ital,wght@0,300;0,400;0,700;0,900;1,400&display=swap" rel="stylesheet">
<style>
:root{
  --navy:#142a44;
  --navy-deep:#0f2036;
  --white:#ffffff;
  --ink:#1d1d1d;
  --muted:#9aa3ad;
  --silver-a:#f4f4f4;
  --silver-b:#c9c9c9;
  --charcoal:#3b3b3d;
  --blue-a:#2f6fb6;
  --blue-b:#123f7a;
  --canvas:#ececec;
}
*{margin:0;padding:0;box-sizing:border-box}
html,body{width:800px;height:1200px;overflow:hidden}
body{background:var(--canvas);font-family:'Lato',sans-serif;color:var(--ink);position:relative}
.page{position:absolute;top:331px;width:380px;height:537px;overflow:hidden;box-shadow:0 2px 8px rgba(0,0,0,.18);background:var(--white)}
.page--front{left:14px}
.page--back{left:406px}
.col{position:absolute;top:0;height:100%}
p,li{font-size:6px;line-height:1.35}
ul{list-style:none}
.bullets li{position:relative;padding-left:9px;margin-bottom:3px}
.bullets li::before{content:"";position:absolute;left:1px;top:2.3px;width:3px;height:3px;border-radius:50%;background:currentColor}
.h-small{font-size:8px;font-weight:900;text-transform:uppercase;line-height:1.15;margin-bottom:5px}

/* front */
.front-side{left:0;width:188px;background:var(--navy);color:var(--white);padding:16px 14px}
.brand{text-align:center;margin-bottom:16px}
.brand__mark{width:22px;height:22px;border-radius:50%;background:var(--white);margin:0 auto 8px}
.brand__name{font-size:6.5px;letter-spacing:2px;font-weight:400}
.title__lead{font-size:17px;font-weight:300;letter-spacing:.3px;line-height:1.1}
.title__main{font-size:18px;font-weight:900;line-height:1.05}
.title__main--grey{color:var(--muted)}
.quote{font-size:7px;font-style:italic;margin:12px 0 8px;line-height:1.3}
.quote-author{font-size:10px;font-weight:700;margin-bottom:12px}
.front-side p{margin-bottom:8px}
.front-side .h-small{margin-top:6px}
.email-bar{position:absolute;left:0;top:468px;width:188px;height:22px;background:var(--white);color:var(--ink);font-size:8px;font-weight:700;display:flex;align-items:center;padding-left:14px}
.front-main{left:188px;width:192px}
.front-photo{position:absolute;inset:0;background:linear-gradient(180deg,#f4f2ee 0%,#ece6da 35%,#d9c7a6 62%,#b79c73 82%,#6f5c44 100%)}
.front-questions{position:relative;padding:14px 12px 0 10px}
.front-questions .intro{margin-bottom:6px}

/* back */
.back-side{left:0;width:180px;background:var(--navy-deep);color:var(--white)}
.back-photo{height:232px;background:linear-gradient(120deg,#6a3b26 0%,#3d2a22 45%,#1d1b1e 100%)}
.benefits{padding:10px 12px}
.benefits .intro{margin-bottom:7px}
.benefits .outro{margin-top:10px}
.back-main{left:180px;width:200px;background:linear-gradient(160deg,var(--silver-a) 0%,var(--silver-b) 55%,#e4e4e4 100%);padding:14px 10px 0}
.dates{width:100%;border-collapse:collapse;margin-bottom:14px;background:rgba(255,255,255,.55)}
.dates td{font-size:5.5px;padding:2.3px 4px;border-bottom:1px solid #d3d3d3}
.dates td:last-child{text-align:right}
.back-main .h-small{margin-top:4px}
.back-main p{margin-bottom:12px}
.back-main .bullets{margin-bottom:14px}
.price{width:148px;height:46px;margin:2px auto 14px;border-radius:6px;background:linear-gradient(180deg,var(--blue-a),var(--blue-b));color:var(--white);text-align:center;padding-top:4px;border:2px solid #dfe6ef}
.price__amount{font-size:22px;font-weight:900;line-height:1}
.price__note{font-size:11px;font-weight:700;line-height:1.1}
.terms-title{font-size:5.5px;font-weight:700;margin-bottom:2px}
.terms{font-size:4.6px!important;line-height:1.3}
.contact{position:absolute;left:0;bottom:0;width:200px;height:118px;background:var(--charcoal);color:var(--white);padding:14px 10px}
.contact p{margin-bottom:1px}
.contact .row{display:flex;align-items:center;gap:4px}
.contact svg{width:6px;height:6px;flex:none}
</style>
</head>
<body>

<section class="page page--front">
  <div class="col front-side">
    <div class="brand">
      <div class="brand__mark"></div>
      <div class="brand__name">LUMENA GROUP</div>
    </div>
    <div class="title__lead">5 DAY PROGRAM</div>
    <div class="title__main">UNTANGLING THE</div>
    <div class="title__main title__main--grey">FAMILY PATTERN</div>
    <p class="quote">"If you cannot get rid of the family skeleton, you may as well make it dance"</p>
    <div class="quote-author">Edmund Harrow Vale</div>
    <p>"Untangling the Family Pattern" and breaking out of your adapted family roles is one of the most important things you can do to feel happy with yourself and in your relationships</p>
    <p>Participating in Untangling the Family Pattern will help you uncover the unconscious psychological defences, which create destructive habits and behaviour patterns that keep you stuck; recycling the same unfulfilling relationships, circumstances and patterns in your life.</p>
    <div class="h-small">Maybe it's time to think about what you can undo!</div>
    <p>If you answered yes to any of the above questions, it's likely that you are carrying a family legacy and a family role from your formative years that does not belong to you. If you seem to be sabotaging your success these roles and unconscious family patterns may very well be getting in the way of your happiness and well being.</p>
  </div>
  <div class="email-bar">marjorie@thelumenagroup.example</div>
  <div class="col front-main">
    <div class="front-photo" role="img" aria-label="Silhouette of a family at sunset, a parent lifting a child into the air"></div>
    <div class="front-questions">
      <div class="h-small">How do you know if you need to break free?</div>
      <p class="intro">Consider the following questions:</p>
      <ul class="bullets">
        <li>Do you struggle to meet your own needs and wants, placing friends and family first?</li>
        <li>Do you adapt to fit in, be liked or accepted?</li>
        <li>Are you the one who is overly responsible for others or at work?</li>
        <li>Are you an over achiever only to find you are never satisfied with the end result?</li>
        <li>Do you suffer from repetitive, frustrating situations and unhealthy behaviours in your personal and professional relationships?</li>
        <li>Are you "the one" who listens to others download their problems?</li>
        <li>Do you feel uncomfortable, asking others for help?</li>
        <li>Are you tired of being invisible?</li>
        <li>Do you find yourself feeling compelled to distract others, or use humour to ease emotional tension?</li>
        <li>Are you tired of searching for what you can DO or acquire to feel happy and satisfied?</li>
      </ul>
    </div>
  </div>
</section>

<section class="page page--back">
  <div class="col back-side">
    <div class="back-photo" role="img" aria-label="Hooded figure walking past a red brick wall at dusk"></div>
    <div class="benefits">
      <div class="h-small">Program Benefits</div>
      <p class="intro">During the program you will learn how to:</p>
      <ul class="bullets">
        <li>Recognise the ways you adapt, so you can undo the false you and unleash the true you.</li>
        <li>Identify what you need to do for yourself to stop destructive behaviour patterns.</li>
        <li>Uncover important values that will bring you deep fulfilment.</li>
        <li>Speak up and be heard.</li>
        <li>Be present and be seen.</li>
        <li>Ask for help without feeling too embarrassed or vulnerable.</li>
        <li>Manage your emotions, rather than everyone else's.</li>
        <li>Share responsibility with others and have more equal relationships.</li>
        <li>Discover what you really need and want, and learn the strategy of creating a vision.</li>
        <li>Discover what your true needs are and work on getting them met.</li>
      </ul>
      <p class="outro">History doesn't have to repeat itself! The program is specifically designed for those of you who are ready to address the CORE ISSUES that prevent you from experiencing success, freedom and deep fulfilment in your relationships and in your life.</p>
    </div>
  </div>
  <div class="col back-main">
    <div class="h-small">Program Details</div>
    <table class="dates">
      <tr><td>Thursday 24th January</td><td>9:00am - 5:00pm</td></tr>
      <tr><td>Friday, 25th January</td><td>9:00am - 5:00pm</td></tr>
      <tr><td>Saturday, 26th January</td><td>9:00am - 5:00pm</td></tr>
      <tr><td>Sunday, 27th January</td><td>9:00am - 5:00pm</td></tr>
      <tr><td>Monday, 28th October</td><td>9:00am - 5:00pm</td></tr>
    </table>
    <div class="h-small">Enrolment Process</div>
    <p><strong>Enrolments close Friday, 18th January 2019. To book your place, register your interest or find out more about this program please call MARJORIE 0400 000 123.</strong></p>
    <div class="h-small">Inclusions</div>
    <ul class="bullets">
      <li>A pre-program phone consult. Relevant on-line diagnostic survey's.</li>
      <li>Integrated Equine Assisted Psychotherapy.</li>
      <li>Art Therapy Piece.</li>
      <li>All course materials (notebook, writing materials).</li>
      <li>Morning and afternoon tea daily + light lunch.</li>
    </ul>
    <div class="h-small">Investments</div>
    <div class="price">
      <div class="price__amount">$2400</div>
      <div class="price__note">including GST</div>
    </div>
    <div class="terms-title">TERMS &amp; CONDITIONS</div>
    <p class="terms">A non-refundable deposit of $800 is required to hold your place. Full payment is required by Friday 18th January 2019. A 3.3% surcharge applies to card transactions. EFTPOS facility available.</p>
    <div class="contact">
      <p>The Lumena Group Pty Ltd</p>
      <p>ABN 12 345 678 901</p>
      <p class="row"><svg viewBox="0 0 10 10"><path d="M5 0a3.5 3.5 0 0 0-3.5 3.5C1.5 6 5 10 5 10s3.5-4 3.5-6.5A3.5 3.5 0 0 0 5 0zm0 5a1.4 1.4 0 1 1 0-2.8A1.4 1.4 0 0 1 5 5z" fill="#fff"/></svg>Fernhill Lane, Brookvale NSW 2999</p>
      <p class="row"><svg viewBox="0 0 10 10"><rect x="2.5" y="0.5" width="5" height="9" rx="1" fill="#fff"/><rect x="3.3" y="1.6" width="3.4" height="5.6" fill="#3b3b3d"/></svg>0400 000 123</p>
      <p class="row"><svg viewBox="0 0 10 10"><rect x="0.5" y="2" width="9" height="6" fill="#fff"/><path d="M0.5 2 5 5.5 9.5 2" stroke="#3b3b3d" stroke-width="0.8" fill="none"/></svg>marjorie@thelumenagroup.example</p>
    </div>
  </div>
</section>

</body>
</html>
```